Learning Habits- Teaching and Learning Policy

Hi,

The philosophy behind this Teaching and Learning Policy is to equip young people (Age 16-18) for many challenges that lies ahead. The pace of technological advancement is so great that it is probable that many jobs our students will do in their lifetime do not yet even exist. We realise that we need to help develop our students into effective lifelong learners – meaning that they will:

-Need to be independent whilst also being able to work as a team.
-Need to apply many different strategies to help take on new concepts.
-Reflect on current practice, and improve.

I have attached the file which has the basic designs of the 4 different leaner habits and what they entail. Each habit is colour coordinated, so please keep the colours the same.

Collaboration- Blue (royal blue)
Persevering- Red
Planning- Orange
Reflection- Yellow

I would ideally like the poster to be transferable into a powerpoint too.

Thanking you all so much.

Perla
Updates

Project Deadline Extended Reason: Hi,I am extending this deadline as I will be requesting some changes to the title / slogan.I need the four learning habits have a catchy name which will motivate students.Please send me some suggestions.Thanking you all.Perla Added Monday, March 28, 2016

Target Market(s)

Teachers and students (age 16-18)

Industry/Entity Type

Education

Font styles to use
Other font styles liked:
• Something friendly to kids- where the a is printed like it is written. Similar to century gothic but more friendly.

Requirements
Must have
• Laid out similar to the the website attached. Interesting, motivational yet educational to students in how they can become lifelong learners.
Nice to have
• I should be able to transfer this to a powerpoint from a poster.
• It can be four posters or one depending on the design.
Should not have
• Each Habit must be colour-coordinated:
• Collaboration- Blue (royal blue)
• Persevering- Red
• Planning- Orange
• Reflection- Yellow
• Thank you,

```html
<!DOCTYPE html>
<html lang="en">
<head>
<meta charset="utf-8">
<title>Learning Habits – Teaching and Learning Policy</title>
<link rel="stylesheet" href="https://fonts.googleapis.com/css2?family=Poppins:wght@400;600;700&display=swap">
<style>
  :root {
    --bg: #3c3c3c;
    --ink: #ffffff;
    --ink-soft: #f2f2f2;
    --blue: #1b2fd6;
    --blue-tone: #3446e0;
    --red: #e6141c;
    --red-tone: #c80f16;
    --orange: #f57a10;
    --orange-tone: #fb9a3d;
    --yellow: #f3c51c;
    --yellow-tone: #f9dc63;
  }
  * { margin: 0; padding: 0; box-sizing: border-box; }
  html, body { width: 870px; height: 1200px; overflow: hidden; background: var(--bg); }
  .poster {
    position: relative;
    width: 870px;
    height: 1200px;
    background: var(--bg);
    font-family: "Poppins", "Century Gothic", sans-serif;
    color: var(--ink);
    overflow: hidden;
  }
  .poster-header { position: absolute; top: 92px; left: 0; width: 100%; text-align: center; }
  .poster-title { font-size: 38px; font-weight: 700; letter-spacing: 0.2px; line-height: 1.2; }
  .poster-subtitle { font-size: 30px; font-weight: 400; margin-top: 4px; color: var(--ink-soft); }
  .poster-footer {
    position: absolute; top: 1078px; left: 0; width: 100%;
    text-align: center; font-size: 30px; font-weight: 400; color: var(--ink-soft);
  }

  /* Teardrop petals: a square with three rounded corners, rotated so the sharp corner faces the centre */
  .petal { position: absolute; border-radius: 50%; }
  .petal--collaboration {
    left: 265px; top: 270px; width: 340px; height: 340px;
    background: var(--blue); border-bottom-right-radius: 0; transform: rotate(45deg); z-index: 1;
  }
  .petal--persevering {
    left: 542px; top: 472px; width: 296px; height: 296px;
    background: var(--red); border-top-left-radius: 0; transform: rotate(-45deg); z-index: 2;
  }
  .petal--planning {
    left: 32px; top: 492px; width: 296px; height: 296px;
    background: var(--orange); border-top-right-radius: 0; transform: rotate(45deg); z-index: 2;
  }
  .petal--reflection {
    left: 285px; top: 700px; width: 300px; height: 300px;
    background: var(--yellow); border-top-left-radius: 0; transform: rotate(45deg); z-index: 3;
  }

  .habit { position: absolute; text-align: center; z-index: 5; }
  .habit-name { font-size: 30px; font-weight: 700; line-height: 1.15; }
  .habit-traits { list-style: none; font-size: 19px; font-weight: 400; line-height: 1.3; margin-top: 4px; }

  .habit--collaboration { left: 285px; top: 458px; width: 300px; }
  .habit--persevering { left: 560px; top: 628px; width: 270px; }
  .habit--planning { left: 40px; top: 690px; width: 240px; text-align: left; padding-left: 30px; }
  .habit--reflection { left: 285px; top: 880px; width: 300px; }

  .habit-visual { position: absolute; z-index: 4; border-radius: 18px; }
  .habit-visual--collaboration { left: 355px; top: 300px; width: 160px; height: 140px; background: linear-gradient(180deg, #ffffff 0%, #d8d8e6 100%); opacity: 0.9; }
  .habit-visual--persevering { left: 640px; top: 520px; width: 150px; height: 90px; background: linear-gradient(160deg, #ffffff 0%, #3a3a3a 100%); opacity: 0.85; }
  .habit-visual--planning { left: 80px; top: 560px; width: 130px; height: 120px; background: linear-gradient(160deg, #ffffff 0%, var(--orange-tone) 100%); }
  .habit-visual--reflection { left: 375px; top: 760px; width: 120px; height: 90px; border-radius: 45px; background: #ffffff; }
</style>
</head>
<body>
<main class="poster">
  <header class="poster-header">
    <h1 class="poster-title">Learning Habits</h1>
    <p class="poster-subtitle">Teaching and Learning Policy</p>
  </header>

  <div class="petal petal--collaboration"></div>
  <div class="petal petal--planning"></div>
  <div class="petal petal--persevering"></div>
  <div class="petal petal--reflection"></div>

  <div class="habit-visual habit-visual--collaboration" role="img" aria-label="Illustration of people holding up puzzle pieces together"></div>
  <div class="habit-visual habit-visual--persevering" role="img" aria-label="Illustration of a figure pushing a boulder up a slope"></div>
  <div class="habit-visual habit-visual--planning" role="img" aria-label="Illustration of a clipboard with a chart and a clock"></div>
  <div class="habit-visual habit-visual--reflection" role="img" aria-label="Illustration of a thought cloud"></div>

  <section class="habit habit--collaboration">
    <h2 class="habit-name">Collaboration</h2>
    <ul class="habit-traits">
      <li>Empathy and Listening</li>
      <li>Interdependence</li>
      <li>Communication</li>
      <li>Questioning</li>
    </ul>
  </section>

  <section class="habit habit--persevering">
    <h2 class="habit-name">Persevering</h2>
    <ul class="habit-traits">
      <li>Managing Distractions</li>
      <li>Meta-Learing</li>
    </ul>
  </section>

  <section class="habit habit--planning">
    <h2 class="habit-name">Planning</h2>
    <ul class="habit-traits">
      <li>Distilling</li>
    </ul>
  </section>

  <section class="habit habit--reflection">
    <h2 class="habit-name">Reflection</h2>
    <ul class="habit-traits">
      <li>Monitoring</li>
      <li>Evaluating</li>
    </ul>
  </section>

  <footer class="poster-footer">Teaching and Learning Policy</footer>
</main>
</body>
</html>
```